Copper Lantern Fitness Flyer

We need a Flyer designed for a Revolutionary Fresh New Functional Fitness facility in Manly Sydney, Australia. We have just recently opened and now need to get the word out. Using the flyers to hand out at events also for shop counters and letterbox drops.

Our company name is Copper Lantern Fitness "Where STRENGTH Becomes Your SPARK".
We promote health and fitness to all fitness levels concentrating on functional fitness. To learn more about us and our colour scheme see attached file and also check us out on www.brightvine-social.example/copperlanternfitnessgroup

A5 Size please

Target Market(s)

The beauty of our system is it is for everyone we have girls and guys in there teens, 20's 30's 40's and 50's. Not only that we have professional athletes, military and high fitness levels all the way to people who are overweight and need to loose weight and tone up. The system caters for everyone.

Industry/Entity Type

Fitness

Requirements
Must have
• FRONT:

Free 30min Fat Blasting Experience With Your Very Own Personal Trainer !!!

New Class Starts Every 3 minutes.
30 minute Workout With A Trainer.
No Machines No Mirrors And No Attitudes.
Catering For All Fitness Levels.
Results Guaranteed Or Your Money Back.
Fun, Fresh, Clean, Revolutionary New Facility.

Back:

You Are Just Moments Away From Burning Fat Faster Than Ever Before And Getting That Body You Always Wanted !!!

Come In Today To Claim Your FREE Workout.

Ph (02) 9417 2086
Address 5/127 Greywattle Ave Fernbrook 2178
www.brightvine-social.example/copperlanternfitnessgroup
Nice to have
• FRONT:

Back:

Ph (02) 9417 2086

```html
<!DOCTYPE html>
<html lang="en">
<head>
<meta charset="utf-8">
<title>Copper Lantern Fitness Flyer</title>
<link rel="stylesheet" href="https://fonts.googleapis.com/css2?family=Source+Sans+3:wght@400;600;700;900&display=swap">
<style>
  :root {
    --paper: #ffffff;
    --ink: #111111;
    --frame-grey: #4a4a4a;
    --headline-yellow: #fff200;
    --offer-green: #b5cc18;
    --contact-blue: #2e7dc4;
    --accent-red: #e4312b;
    --stripe-yellow: #f6e81a;
    --stripe-blue: #3aa0dc;
    --stripe-red: #e53b33;
    --stripe-green: #9cc83c;
    --brand-grey: #4d4d4d;
  }
  html, body {
    margin: 0;
    padding: 0;
    overflow: hidden;
    background: var(--paper);
  }
  .flyer {
    position: relative;
    width: 846px;
    height: 1200px;
    background: var(--paper);
    overflow: hidden;
    font-family: "Source Sans 3", "Myriad Pro", Arial, sans-serif;
    color: var(--ink);
  }
  .edge-stripes {
    position: absolute;
    inset: 0;
  }
  .panel {
    position: absolute;
    left: 106px;
    width: 630px;
    box-sizing: border-box;
    border: 7px solid var(--frame-grey);
    border-radius: 10px;
    box-shadow: 6px 8px 14px rgba(0,0,0,0.35);
    text-align: center;
  }
  .panel-headline {
    top: 97px;
    height: 257px;
    background: var(--headline-yellow);
    padding-top: 28px;
  }
  .headline-lead {
    margin: 0;
    font-size: 31px;
    font-weight: 400;
    line-height: 1.27;
    letter-spacing: -0.2px;
  }
  .headline-punch {
    margin: 6px 0 0 150px;
    text-align: left;
    font-size: 62px;
    font-weight: 900;
    line-height: 1;
    letter-spacing: -0.5px;
  }
  .panel-offer {
    top: 416px;
    height: 116px;
    background: var(--offer-green);
    padding-top: 18px;
  }
  .offer-text {
    margin: 0;
    font-size: 28px;
    font-weight: 700;
    letter-spacing: -1px;
    line-height: 1.25;
    text-transform: uppercase;
  }
  .offer-text .offer-free {
    font-size: 38px;
  }
  .panel-contact {
    top: 610px;
    height: 213px;
    background: var(--contact-blue);
    padding-top: 44px;
  }
  .contact-line {
    margin: 0;
    font-size: 25px;
    line-height: 1.36;
    color: var(--ink);
  }
  .contact-dot {
    display: inline-block;
    width: 11px;
    height: 11px;
    margin: 0 4px 2px 6px;
    background: var(--accent-red);
  }
  .brand {
    position: absolute;
    left: 214px;
    top: 930px;
    display: flex;
    align-items: center;
    gap: 26px;
  }
  .brand-mark {
    width: 150px;
    height: 150px;
    border-radius: 14px;
    background: var(--offer-green);
  }
  .brand-name {
    margin: 0;
    font-size: 40px;
    font-weight: 700;
    line-height: 1.02;
    letter-spacing: 2px;
    text-transform: uppercase;
    color: var(--brand-grey);
  }
  .brand-rule {
    height: 3px;
    background: var(--brand-grey);
    margin: 8px 0 6px;
  }
  .brand-tagline {
    margin: 0;
    font-size: 17px;
    font-weight: 600;
    color: var(--ink);
  }
</style>
</head>
<body>
<main class="flyer">
  <svg class="edge-stripes" width="846" height="1200" viewBox="0 0 846 1200" aria-hidden="true">
    <g stroke-width="4" fill="none">
      <line x1="0" y1="8"  x2="846" y2="8"  stroke="var(--stripe-yellow)"/>
      <line x1="0" y1="16" x2="846" y2="16" stroke="var(--stripe-blue)"/>
      <line x1="0" y1="24" x2="846" y2="24" stroke="var(--stripe-yellow)"/>
      <line x1="0" y1="32" x2="846" y2="32" stroke="var(--stripe-red)"/>
      <line x1="0" y1="40" x2="846" y2="40" stroke="var(--stripe-green)"/>

      <line x1="16" y1="0" x2="16" y2="1200" stroke="var(--stripe-yellow)"/>
      <line x1="24" y1="0" x2="24" y2="1200" stroke="var(--stripe-blue)"/>
      <line x1="32" y1="0" x2="32" y2="1200" stroke="var(--stripe-yellow)"/>
      <line x1="40" y1="0" x2="40" y2="1200" stroke="var(--stripe-red)"/>

      <line x1="806" y1="0" x2="806" y2="1200" stroke="var(--stripe-red)"/>
      <line x1="814" y1="0" x2="814" y2="1200" stroke="var(--stripe-yellow)"/>
      <line x1="822" y1="0" x2="822" y2="1200" stroke="var(--stripe-blue)"/>
      <line x1="830" y1="0" x2="830" y2="1200" stroke="var(--stripe-yellow)"/>
    </g>
  </svg>

  <section class="panel panel-headline">
    <p class="headline-lead">YOU ARE JUST MOMENTS AWAY FROM<br>BURNING FAT FASTER THAN EVER BEFORE<br>AND GETTING THAT BODY YOU ALWAYS</p>
    <p class="headline-punch">WANTED !!!</p>
  </section>

  <section class="panel panel-offer">
    <p class="offer-text">Come in today to claim your<br><span class="offer-free">Free</span> workout.</p>
  </section>

  <section class="panel panel-contact">
    <p class="contact-line">Ph<span class="contact-dot"></span>(02) 9417 2086</p>
    <p class="contact-line">Address<span class="contact-dot"></span>5/127 Greywattle Ave Fernbrook 2178</p>
    <p class="contact-line">www.brightvine-social.example/copperlanternfitnessgroup</p>
  </section>

  <div class="brand">
    <div class="brand-mark" aria-hidden="true"></div>
    <div class="brand-wordmark">
      <p class="brand-name">Copper<br>Lantern<br>Fitness</p>
      <div class="brand-rule"></div>
      <p class="brand-tagline">Where Strength Becomes Your Spark</p>
    </div>
  </div>
</main>
</body>
</html>
```